Lanternfield Disability - Social Security Disability Attorneys

Our company is expanding to attract clients nationwide for our social security disability practice. We have a logo, but I am looking for a creative and elegant letterhead that projects an image of being technologically advanced but still professional enough for the legal field. I am looking for the "wow factor" combined with this is still professional enough for a law practice.

Requesting letterhead and business card design
Updates

Had to update and change the logo. The previous logo had a typo. Please send updates with the new logo for consideration. The letterhead and business cards should be professional enough to be used for a law firm. Thanks.

Industry/Entity Type

Law Practice, Law Firm, Healthcare Industry, Government

Colors

Designer to choose colors to be used in the design.

Requirements
Nice to have
• **Please create a vertical design for the business card**

```html
<!DOCTYPE html>
<html lang="en">
<head>
<meta charset="utf-8">
<title>Lanternfield Disability – Stationery</title>
<link href="https://fonts.googleapis.com/css2?family=Open+Sans:wght@400;600;700&family=Varela+Round&display=swap" rel="stylesheet">
<style>
  :root {
    --stage: #26292d;
    --paper: #ffffff;
    --brand-blue: #1a3fb0;
    --sky: #1e9be8;
    --sky-light: #4ab8f0;
    --orange: #f47c10;
    --orange-light: #ffa451;
    --ink-grey: #5b5f66;
    --tint-blue: #d6ebfa;
    --tint-orange: #fde6d2;
    --tint-grey: #ececec;
  }
  * { box-sizing: border-box; margin: 0; padding: 0; }
  html, body { width: 1200px; height: 960px; overflow: hidden; }
  body {
    background: var(--stage);
    font-family: "Open Sans", sans-serif;
    position: relative;
  }

  /* Letterhead */
  .letterhead {
    position: absolute; left: 71px; top: 41px;
    width: 621px; height: 878px;
    background: var(--paper);
    overflow: hidden;
  }
  .letterhead__tiles span { position: absolute; display: block; }
  .letterhead__name {
    position: absolute; left: 20px; top: 60px;
    font-family: "Open Sans", sans-serif; font-weight: 600;
    font-size: 23px; color: var(--brand-blue); letter-spacing: 0.2px;
  }
  .letterhead__contact {
    position: absolute; left: 283px; top: 36px;
    font-size: 8px; font-weight: 600; line-height: 14px;
  }
  .letterhead__contact .line { display: flex; align-items: center; gap: 3px; white-space: nowrap; }
  .letterhead__contact .line--address { color: var(--sky); }
  .letterhead__contact .line--reach { color: var(--ink-grey); }
  .dot { display: inline-block; width: 7px; height: 7px; border-radius: 50%; border: 1.5px solid var(--orange-light); }
  .dot--fill { background: var(--orange-light); border: none; }
  .letterhead__band { position: absolute; left: 273px; right: 0; }
  .letterhead__band--blue { top: 65px; height: 6px; background: var(--sky); }
  .letterhead__band--orange { top: 75px; height: 7px; background: var(--orange); }
  .letterhead__footer { position: absolute; left: 0; bottom: 0; width: 621px; height: 8px; }

  /* Card front */
  .card-front {
    position: absolute; left: 639px; top: 215px;
    width: 243px; height: 405px;
    background: linear-gradient(165deg, var(--orange) 0%, var(--orange-light) 28%, #c9b79a 48%, #8ec7e2 68%, var(--sky-light) 85%, var(--sky) 100%);
    text-align: center;
  }
  .card-front__name {
    position: absolute; left: 0; right: 0; top: 208px;
    font-weight: 600; font-size: 19px; color: var(--brand-blue);
  }
  .card-front__web {
    position: absolute; left: 0; right: 0; top: 359px;
    font-size: 12.5px; color: #ffffff;
  }

  /* Card back */
  .card-back {
    position: absolute; left: 915px; top: 503px;
    width: 242px; height: 404px;
    background: var(--paper);
  }
  .card-back__name {
    position: absolute; left: 0; right: 0; top: 104px; text-align: center;
    font-weight: 600; font-size: 19px; color: var(--brand-blue);
  }
  .card-back__person { position: absolute; left: 23px; top: 170px; }
  .card-back__person-name { font-family: "Varela Round", sans-serif; font-size: 16px; color: var(--orange); }
  .card-back__role { font-family: "Varela Round", sans-serif; font-size: 10px; color: var(--ink-grey); margin-top: 1px; }
  .card-back__rail {
    position: absolute; left: 37px; top: 243px; width: 18px; height: 161px;
    background: linear-gradient(180deg, var(--sky) 0%, var(--sky-light) 30%, #b9c7c6 55%, var(--orange-light) 75%, var(--orange) 100%);
  }
  .card-back__contacts { position: absolute; left: 37px; top: 245px; list-style: none; }
  .card-back__contacts li {
    display: flex; align-items: center; height: 20px;
    font-size: 9.5px; color: var(--ink-grey);
  }
  .card-back__contacts .icon { width: 18px; display: flex; justify-content: center; }
  .card-back__contacts .text { padding-left: 4px; white-space: nowrap; }
  .card-back__contacts .accent { color: var(--orange); font-weight: 700; }
</style>
</head>
<body>

<section class="letterhead" aria-label="Letterhead">
  <div class="letterhead__tiles" aria-hidden="true">
    <span style="left:512px;top:0;width:30px;height:22px;background:var(--tint-orange)"></span>
    <span style="left:573px;top:0;width:48px;height:30px;background:var(--tint-blue)"></span>
    <span style="left:512px;top:27px;width:30px;height:54px;background:var(--tint-grey)"></span>
    <span style="left:547px;top:30px;width:26px;height:42px;background:var(--paper)"></span>
    <span style="left:546px;top:30px;width:48px;height:131px;background:var(--tint-blue)"></span>
    <span style="left:598px;top:50px;width:23px;height:24px;background:var(--tint-orange)"></span>
    <span style="left:512px;top:84px;width:30px;height:20px;background:var(--tint-orange)"></span>
  </div>
  <div class="letterhead__name">Lanternfield Disability</div>
  <div class="letterhead__contact">
    <div class="line line--address"><span class="dot"></span> 0000 Example , Ste 135, California, 93103, United States</div>
    <div class="line line--reach"><span class="dot"></span> (000) 000-0000 <span class="dot dot--fill"></span> info@lanternfielddisability.com <span class="dot dot--fill"></span> www.lanternfielddisability.com</div>
  </div>
  <div class="letterhead__band letterhead__band--blue"></div>
  <div class="letterhead__band letterhead__band--orange"></div>
  <svg class="letterhead__footer" viewBox="0 0 621 8" aria-hidden="true">
    <polygon points="0,0 256,0 252,8 0,8" fill="#1e9be8"/>
    <polygon points="262,0 482,0 478,8 258,8" fill="#f47c10"/>
    <polygon points="488,0 621,0 621,8 484,8" fill="#1e9be8"/>
  </svg>
</section>

<section class="card-front" aria-label="Business card front">
  <div class="card-front__name">Lanternfield Disability</div>
  <div class="card-front__web">www.lanternfielddisability.com</div>
</section>

<section class="card-back" aria-label="Business card back">
  <div class="card-back__name">Lanternfield Disability</div>
  <div class="card-back__person">
    <div class="card-back__person-name">Example Name</div>
    <div class="card-back__role">Designation</div>
  </div>
  <div class="card-back__rail" aria-hidden="true"></div>
  <ul class="card-back__contacts">
    <li><span class="icon"><svg width="10" height="10" viewBox="0 0 10 10"><circle cx="5" cy="5" r="4.5" fill="#fff"/><path d="M5 2.2a1.8 1.8 0 0 1 1.8 1.8C6.8 5.4 5 7.6 5 7.6S3.2 5.4 3.2 4A1.8 1.8 0 0 1 5 2.2z" fill="#1e3a5a"/></svg></span><span class="text accent">Level 00, 00 Example Street,</span></li>
    <li><span class="icon"></span><span class="text accent">Example 000 US</span></li>
    <li><span class="icon"><svg width="10" height="10" viewBox="0 0 10 10"><circle cx="5" cy="5" r="4.5" fill="#fff"/><path d="M2.6 4.2h4.8v2.6H2.6zM3.4 3.2h3.2v1H3.4z" fill="#1e3a5a"/></svg></span><span class="text">0000 000 129</span></li>
    <li><span class="icon"><svg width="10" height="10" viewBox="0 0 10 10"><circle cx="5" cy="5" r="4.5" fill="#fff"/><rect x="2.7" y="3.4" width="4.6" height="3.2" fill="#1e3a5a"/></svg></span><span class="text">contact@lanternfielddisability.com</span></li>
    <li><span class="icon"><svg width="10" height="10" viewBox="0 0 10 10"><circle cx="5" cy="5" r="4.5" fill="#fff"/><circle cx="5" cy="5" r="2.6" fill="none" stroke="#1e3a5a" stroke-width="0.9"/><path d="M2.4 5h5.2M5 2.4v5.2" stroke="#1e3a5a" stroke-width="0.7"/></svg></span><span class="text">www.lanternfielddisability.com</span></li>
  </ul>
</section>

</body>
</html>
```